Tervolan Pty Ltd professional business card

A professional business card template using the colours from the supplied logo.
Clean crisp lines while, Modern while not being over the top.

Target Market(s)

Construction, commerical and industrial

Industry/Entity Type

Communications

Contact Information for Business Card

For a Communications, IT, Optical fibre installation company

Colors
37b8a4

```html
<!DOCTYPE html>
<html lang="en">
<head>
<meta charset="utf-8">
<title>Tervolan Pty Ltd – Business Card</title>
<link rel="stylesheet" href="https://fonts.googleapis.com/css2?family=Josefin+Sans:wght@300;400;600&display=swap">
<style>
  :root {
    --teal: #128893;
    --grey: #646567;
    --card: #f4f4f4;
    --backdrop: #e6e6e6;
    --white: #ffffff;
  }
  * { margin: 0; padding: 0; box-sizing: border-box; }
  html, body {
    width: 1200px; height: 1200px; overflow: hidden;
    background: var(--backdrop);
    font-family: "Josefin Sans", sans-serif;
  }
  .card {
    position: absolute;
    left: 227px;
    width: 746px;
    height: 425px;
    overflow: hidden;
  }
  .card-front { top: 135px; background: var(--card); }
  .card-back  { top: 640px; background: var(--teal); }

  .corner-accent {
    position: absolute;
    left: 380px; top: 322px;
    width: 366px; height: 103px;
    background: linear-gradient(to right, rgba(18,136,147,0) 0%, var(--teal) 40%);
  }

  .wordmark {
    position: absolute;
    font-weight: 600;
    text-transform: uppercase;
    line-height: 1;
    white-space: nowrap;
  }
  .card-front .wordmark {
    left: 37px; top: 68px;
    font-size: 66px;
    color: var(--grey);
    letter-spacing: 1px;
  }
  .card-back .wordmark {
    left: 0; right: 0; top: 178px;
    text-align: center;
    font-size: 84px;
    color: var(--white);
    letter-spacing: 2px;
  }

  .person {
    position: absolute;
    right: 38px; top: 82px;
    text-align: right;
  }
  .person-name {
    font-size: 27px; font-weight: 600;
    color: var(--teal);
    letter-spacing: 1px;
    line-height: 1;
  }
  .person-role {
    margin-top: 9px;
    font-size: 19px; font-weight: 300;
    color: var(--grey);
    letter-spacing: 1px;
  }

  .address {
    position: absolute;
    left: 37px; top: 274px;
    font-size: 19px; font-weight: 300;
    color: var(--grey);
    line-height: 27px;
    letter-spacing: 1px;
    font-style: normal;
  }
  .contact {
    position: absolute;
    left: 37px; top: 345px;
    list-style: none;
    font-size: 19px; font-weight: 300;
    color: var(--grey);
    letter-spacing: 1px;
  }
  .contact li {
    display: flex; align-items: center;
    height: 25px;
  }
  .contact svg { width: 18px; height: 18px; margin-right: 10px; }

  .website {
    position: absolute;
    right: 38px; top: 368px;
    font-size: 18px; font-weight: 300;
    color: var(--white);
    letter-spacing: 1.5px;
  }
</style>
</head>
<body>

<section class="card card-front" aria-label="Business card front">
  <div class="corner-accent" role="img" aria-label="Teal corner accent area"></div>

  <div class="wordmark">Tervolan</div>

  <div class="person">
    <div class="person-name">DARA WHITLOCK</div>
    <div class="person-role">Managing Director</div>
  </div>

  <address class="address">
    2871 Marlowe Ave<br>
    Lindhurst , CA 90512
  </address>

  <ul class="contact">
    <li>
      <svg viewBox="0 0 18 18" aria-hidden="true">
        <circle cx="9" cy="9" r="9" fill="var(--teal)"/>
        <path d="M4.5,7.5 C5,5 13,5 13.5,7.5 L11.5,8 L11,6.8 L7,6.8 L6.5,8 Z" fill="var(--white)"/>
        <rect x="5.5" y="8.5" width="7" height="4" rx="1" fill="var(--white)"/>
        <circle cx="9" cy="10.5" r="1.2" fill="var(--teal)"/>
      </svg>
      000 000 00 00
    </li>
    <li>
      <svg viewBox="0 0 18 18" aria-hidden="true">
        <circle cx="9" cy="9" r="9" fill="var(--teal)"/>
        <rect x="4.5" y="5.8" width="9" height="6.4" fill="none" stroke="var(--white)" stroke-width="1.1"/>
        <path d="M4.5,5.8 L9,9.6 L13.5,5.8" fill="none" stroke="var(--white)" stroke-width="1.1"/>
      </svg>
      info@tervolan.com
    </li>
  </ul>

  <div class="website">www.tervolan.com</div>
</section>

<section class="card card-back" aria-label="Business card back">
  <div class="wordmark">Tervolan</div>
</section>

</body>
</html>
```